QELTrill Brochure Design Project

See qeltrill.example website for design elements. We need a sales brochure that can be emailed or given to those prospects seeking "more information".

Our clients are primarily restaurants, both chains and independents. We sell "social media shopper reports on-demand" as a SaaS product by street address. Also, if a client has a chain of restaurants operating under a single brand name, we can "roll" them up into a consolidated report. They can compare restaurants and then group them by region or city...etc. A company can also roll-up a competitor then compare with their own restaurants...by location, region, state, group, etc.

We use a powerful Customer Intelligence Platform to listen to conversations taking place about a brand (at the street address) on the social web. Our technology scours the social web on review sites, search engines, grabs RSS feeds and API's.

The primary prospect are restaurant operators, secondarily retailers in the US. But, we have multiple applications based on use case. Like use QELTrill® for due diligence. The client/prospect is banks, investment banks, investors and lenders seeking customer insights about a possible investment or loan.
Updates

I added logos. The NapWig logo is the main company logo. QELTrill is the product. Color scheme can be found on NapWig.example and QELTrill.example.

I'll need consistent branding around website, cards, other products as well later

Industry/Entity Type

Restaurant

Requirements
Nice to have
• Different uses for financial services, restaurants, retailers, hoteliers, franchisees.

```html
<!DOCTYPE html>
<html lang="en">
<head>
<meta charset="utf-8">
<title>QELTrill Brochure</title>
<link rel="stylesheet" href="https://fonts.googleapis.com/css2?family=Oswald:wght@300;500;700&family=PT+Sans+Narrow:wght@400;700&display=swap">
<style>
  :root {
    --ink: #111111;
    --red: #d71f2b;
    --beige: #c9b48c;
    --beige-light: #e4d8bf;
    --body: #5a5a5a;
    --sub: #6b6b6b;
    --paper: #ffffff;
    --canvas: #ffffff;
    --art-grey: #eef2f5;
  }
  * { margin: 0; padding: 0; box-sizing: border-box; }
  html, body { width: 1200px; height: 834px; overflow: hidden; background: var(--canvas); }
  .spread { position: relative; width: 1200px; height: 834px; }

  .page {
    position: absolute; top: 19px; height: 802px; overflow: hidden;
    background: var(--paper);
    box-shadow: 0 0 3px rgba(0,0,0,.18);
  }
  .page--cover { left: 28px; width: 561px; background: linear-gradient(#f7f7f7, #ffffff 45%); }
  .page--inside { left: 617px; width: 575px; }

  .swoosh { position: absolute; left: 0; top: 0; width: 100%; height: 100%; }

  .brand { position: absolute; left: 22px; top: 32px; display: flex; align-items: center; gap: 12px; }
  .brand__mark { width: 62px; height: 62px; background: var(--red); border-radius: 6px; }
  .brand__name { font-family: "PT Sans Narrow", sans-serif; font-weight: 400; font-size: 36px; color: var(--ink); letter-spacing: .5px; }

  .art { position: absolute; }
  .art--network {
    left: 34px; top: 106px; width: 452px; height: 332px;
    background: radial-gradient(ellipse at 50% 45%, #d6e5f2 0%, var(--art-grey) 55%, rgba(238,242,245,0) 75%);
  }
  .art--icons {
    left: 271px; top: 600px; width: 304px; height: 202px;
    background: radial-gradient(ellipse at 55% 55%, #dfe6ee 0%, #f1f4f7 55%, rgba(255,255,255,0) 80%);
  }

  .headline { position: absolute; font-family: "Oswald", sans-serif; font-weight: 700; text-transform: uppercase; color: var(--ink); }
  .headline .accent { color: var(--red); }
  .headline--cover { left: 22px; top: 520px; font-size: 43px; line-height: 50px; letter-spacing: -.3px; }
  .headline--inside { left: 40px; top: 28px; font-size: 52px; line-height: 47px; letter-spacing: -.3px; }

  .subhead { position: absolute; left: 22px; top: 622px; font-family: "Oswald", sans-serif; font-weight: 300; font-size: 17px; line-height: 28px; color: var(--sub); text-transform: uppercase; }

  .copy { position: absolute; font-family: "PT Sans Narrow", sans-serif; font-size: 8.6px; line-height: 13px; color: var(--body); }
  .copy p + p { margin-top: 10px; }
  .copy--cover-left { left: 22px; top: 700px; width: 282px; }
  .copy--cover-right { left: 330px; top: 582px; width: 226px; }
  .copy--inside { left: 40px; top: 245px; width: 254px; }

  .steps { position: absolute; left: 326px; top: 246px; width: 240px; list-style: none; }
  .step { display: flex; gap: 10px; height: 140px; }
  .step__num { font-family: "Oswald", sans-serif; font-weight: 700; font-size: 62px; line-height: 50px; color: var(--ink); width: 28px; }
  .step__text { font-family: "PT Sans Narrow", sans-serif; font-size: 8.6px; line-height: 13px; color: var(--body); width: 202px; }

  .callout { position: absolute; left: 40px; top: 612px; width: 270px; font-family: "Oswald", sans-serif; font-weight: 500; font-size: 16px; line-height: 23px; color: var(--ink); text-transform: uppercase; }
</style>
</head>
<body>
<main class="spread">

  <section class="page page--cover">
    <div class="art art--network" role="img" aria-label="Illustration of a social network: small figures connected by lines around the words Social Network"></div>

    <svg class="swoosh" viewBox="0 0 561 802" preserveAspectRatio="none" aria-hidden="true">
      <path d="M0 505 C160 560 390 500 561 210 L561 240 C390 530 160 600 0 530 Z" fill="#ececec"/>
      <path d="M0 478 C160 532 380 470 561 182 L561 200 C380 492 160 548 0 490 Z" fill="var(--beige)"/>
      <path d="M0 440 C150 500 380 420 561 140 L561 178 C380 466 150 528 0 472 Z" fill="var(--red)"/>
    </svg>

    <div class="brand">
      <span class="brand__mark"></span>
      <span class="brand__name">QELTrill®</span>
    </div>

    <h1 class="headline headline--cover">Lorem ipsum<br><span class="accent">Dolor sit amet</span></h1>
    <p class="subhead">Phasellus rhoncus tincidunt tellus,<br>a vestibulum nisi feugiat eget</p>

    <div class="copy copy--cover-left">
      <p>Etiam quis turpis massa, a vestibulum neque. Nulla facilisi. Curabitur auctor ullamcorper rhoncus. Vivamus id orci sit amet augue pharetra pretium. Vivamus porttitor faucibus eros, aliquet adipiscing risus euismod in. Aenean ullamcorper blandit posuere.</p>
      <p>Placerat vel, tempor quis sem. Vestibulum egestas leo posuere nulla sodales non placerat lacus suscipit. Phasellus rhoncus tincidunt tellus, a vestibulum nisi feugiat eget. Sed ultrices, orci eget posuere eleifend, ligula odio euismod leo.</p>
    </div>
    <div class="copy copy--cover-right">
      <p>Etiam quis turpis massa, a vestibulum neque. Nulla facilisi. Curabitur auctor ullamcorper rhoncus. Vivamus id orci sit amet augue pharetra pretium. Vivamus porttitor faucibus eros, aliquet adipiscing risus euismod in. Aenean ullamcorper blandit posuere.</p>
      <p>Placerat vel, tempor quis sem. Vestibulum egestas leo posuere nulla sodales non placerat lacus suscipit. Phasellus rhoncus tincidunt tellus, a vestibulum nisi feugiat eget. Sed ultrices, orci eget posuere eleifend, ligula odio euismod leo.</p>
    </div>
  </section>

  <section class="page page--inside">
    <div class="art art--icons" role="img" aria-label="Illustration of connected web service icons forming a network"></div>

    <svg class="swoosh" viewBox="0 0 575 802" preserveAspectRatio="none" aria-hidden="true">
      <path d="M0 110 C50 50 140 14 250 0 L290 0 C170 16 70 52 0 130 Z" fill="var(--beige-light)"/>
      <path d="M0 96 C50 40 130 8 220 0 L250 0 C140 14 50 50 0 110 Z" fill="var(--beige)"/>
      <path d="M0 806 C200 790 390 670 575 612 L575 640 C390 698 200 808 0 820 Z" fill="var(--beige)"/>
      <path d="M0 786 C200 770 390 644 575 580 L575 608 C390 672 200 792 0 806 Z" fill="var(--red)"/>
    </svg>

    <h2 class="headline headline--inside">Lorem ipsum dolor<br><span class="accent">Sit amet, consectetur</span><br>Adipiscing elit</h2>

    <div class="copy copy--inside">
      <p>Etiam quis turpis massa, a vestibulum neque. Nulla facilisi. Curabitur auctor ullamcorper rhoncus. Vivamus id orci sit amet augue pharetra pretium. Vivamus porttitor faucibus eros, aliquet adipiscing risus euismod in. Aenean ullamcorper blandit posuere.</p>
      <p>Placerat vel, tempor quis sem. Vestibulum egestas leo posuere nulla sodales non placerat lacus suscipit. Phasellus rhoncus tincidunt tellus, a vestibulum nisi feugiat eget. Sed ultrices, orci eget posuere eleifend, ligula odio euismod leo.</p>
      <p>Etiam quis turpis massa, a vestibulum neque. Nulla facilisi. Curabitur auctor ullamcorper rhoncus. Vivamus id orci sit amet augue pharetra pretium. Vivamus porttitor faucibus eros, aliquet adipiscing risus euismod in. Aenean ullamcorper blandit posuere.</p>
      <p>Placerat vel, tempor quis sem. Vestibulum egestas leo posuere nulla sodales non placerat lacus suscipit. Phasellus rhoncus tincidunt tellus, a vestibulum nisi feugiat eget. Sed ultrices, orci eget posuere eleifend, ligula odio euismod leo.</p>
    </div>

    <ol class="steps">
      <li class="step"><span class="step__num">1</span><p class="step__text">Orci iaculis nunc. Sed augue nunc, pellentesque quis placerat in, sem. Vestibulum egestas leo posuere nulla sodales non suscipit. Phasellus rhoncus tincidunt tellus, a vestibulum nisi sed ultrices, orci eget posuere eleifend.</p></li>
      <li class="step"><span class="step__num">2</span><p class="step__text">Orci iaculis nunc. Sed augue nunc, pellentesque quis placerat in, sem. Vestibulum egestas leo posuere nulla sodales non suscipit. Phasellus rhoncus tincidunt tellus, a vestibulum nisi sed ultrices, orci eget posuere eleifend.</p></li>
      <li class="step"><span class="step__num">3</span><p class="step__text">Orci iaculis nunc. Sed augue nunc, pellentesque quis placerat in, sem. Vestibulum egestas leo posuere nulla sodales non suscipit. Phasellus rhoncus tincidunt tellus, a vestibulum nisi sed ultrices, orci eget posuere eleifend.</p></li>
    </ol>

    <p class="callout">Lorem ipsum dolor sit amet,<br>consectetur adipiscing elit. In<br>fermentum pretium massa,<br>varius tincidunt era<br>amet. Dolor tellus,<br>cursus at</p>
  </section>

</main>
</body>
</html>
```